Velt Harbor Solutions

I have a file with a logo. It is grainy. I also have a board with my color pallet and other branding items. I need a file with the logo that is high resolution and I also need a business card design.

```html
<!DOCTYPE html>
<html lang="en">
<head>
<meta charset="UTF-8">
<title>Velt Harbor Solutions — Business Card</title>
<link href="https://fonts.googleapis.com/css2?family=Montserrat:wght@400;500;700&family=Open+Sans:wght@700&display=swap" rel="stylesheet">
<style>
  :root {
    --backdrop: #a8a8a8;
    --charcoal: #2a2e35;
    --paper: #f5f8fb;
    --crimson: #8b1c2b;
    --slate: #5f7389;
    --white: #ffffff;
  }
  * { margin: 0; padding: 0; box-sizing: border-box; }
  html, body {
    width: 1200px; height: 1200px; overflow: hidden;
    background: var(--backdrop);
    font-family: "Montserrat", sans-serif;
  }
  .card {
    position: absolute;
    left: 226px;
    width: 755px;
    height: 453px;
  }
  .card-front { top: 114px; background: var(--charcoal); }
  .card-back { top: 638px; background: var(--paper); }

  .person {
    position: absolute; right: 51px; top: 44px; text-align: right;
  }
  .person-name {
    color: var(--white); font-weight: 700; font-size: 31px; letter-spacing: 0.5px; line-height: 1.2;
  }
  .person-role {
    color: var(--crimson); font-weight: 500; font-size: 22px; line-height: 1.2; margin-top: 4px;
  }

  .contact-list {
    position: absolute; right: 51px; top: 314px; list-style: none; text-align: right;
  }
  .contact-item {
    display: flex; justify-content: flex-end; align-items: center; gap: 10px;
    color: var(--white); font-size: 19px; line-height: 30px;
  }
  .contact-icon { width: 17px; height: 17px; fill: var(--crimson); }

  .brand-front {
    position: absolute; left: 30px; width: 270px; top: 318px; text-align: center;
  }
  .brand-front .brand-name {
    color: var(--white); font-weight: 700; font-size: 21px; letter-spacing: 1px; line-height: 1.25;
  }
  .brand-front .brand-tagline {
    color: var(--white); font-family: "Open Sans", sans-serif; font-weight: 700;
    font-size: 7.5px; letter-spacing: 1.5px; margin-top: 18px;
  }

  .brand-back {
    position: absolute; left: 0; right: 0; top: 250px; text-align: center;
  }
  .brand-back .brand-name {
    color: var(--charcoal); font-weight: 700; font-size: 40px; letter-spacing: 2px;
  }
  .brand-back .brand-tagline {
    color: var(--slate); font-family: "Open Sans", sans-serif; font-weight: 700;
    font-size: 13.5px; letter-spacing: 3.5px; margin-top: 44px;
  }
</style>
</head>
<body>
  <section class="card card-front">
    <div class="person">
      <div class="person-name">DANIEL REYES</div>
      <div class="person-role">DIRECTOR</div>
    </div>

    <div class="brand-front">
      <div class="brand-name">VELT HARBOR SOLUTIONS</div>
      <div class="brand-tagline">CLOUD WORKFLOW DEVELOPMENT</div>
    </div>

    <ul class="contact-list">
      <li class="contact-item">
        <svg class="contact-icon" viewBox="0 0 24 24" aria-hidden="true"><path d="M6.6 10.8a15 15 0 0 0 6.6 6.6l2.2-2.2a1 1 0 0 1 1-.25 11.4 11.4 0 0 0 3.6.6 1 1 0 0 1 1 1V20a1 1 0 0 1-1 1A17 17 0 0 1 3 4a1 1 0 0 1 1-1h3.5a1 1 0 0 1 1 1c0 1.25.2 2.45.6 3.6a1 1 0 0 1-.25 1z"/></svg>
        <span>123-456-7890</span>
      </li>
      <li class="contact-item">
        <svg class="contact-icon" viewBox="0 0 24 24" aria-hidden="true"><path d="M2 5h20v14H2z M3 6l9 7 9-7" fill="var(--crimson)" stroke="var(--charcoal)" stroke-width="1.2"/></svg>
        <span>yourbusiness@email.com</span>
      </li>
      <li class="contact-item">
        <svg class="contact-icon" viewBox="0 0 24 24" aria-hidden="true"><circle cx="12" cy="12" r="10"/><path d="M2 12h20M12 2c3 3 3 17 0 20M12 2c-3 3-3 17 0 20M4 7h16M4 17h16" stroke="var(--charcoal)" stroke-width="1.2" fill="none"/></svg>
        <span>www.website.com</span>
      </li>
    </ul>
  </section>

  <section class="card card-back">
    <div class="brand-back">
      <div class="brand-name">VELT HARBOR SOLUTIONS</div>
      <div class="brand-tagline">CLOUD WORKFLOW DEVELOPMENT</div>
    </div>
  </section>
</body>
</html>
```